Flyer Design Project

Business is Wexford In Home Care

We are an Australian provider of In Home Care services.

We have a focus on quality care and a high standard of service.

We are non medical

We want to promote the health, happiness and independence of senior citizens by providing some help at home for general domestic duties (cleaning, bed linnen), personal care (showering, grooming) and meal preparation etc.

Target Market(s)

Seniors (70+) and the Children of seniors.

Industry/Entity Type

Business

Requirements
Must have
• Colour scheme from our website (www.wexfordinhomecare.com.au) –

The uploaded Word doc contains the desired copy.

Leaflet will be a standard A4 size foldout with 6 panels, 3 on each side.

```html
<!DOCTYPE html>
<html lang="en">
<head>
<meta charset="utf-8">
<title>Wexford In Home Care – Trifold Flyer</title>
<link rel="stylesheet" href="https://fonts.googleapis.com/css2?family=Arimo:wght@400;700&display=swap">
<style>
  :root {
    --cream: #fde5c0;
    --sky: #c9daf0;
    --navy: #1f2f5a;
    --text-navy: #1d2b4f;
    --orange: #f7ab2a;
    --tick: #e9a43a;
    --crop: #222222;
    --paper: #ffffff;
  }
  * { box-sizing: border-box; margin: 0; padding: 0; }
  html, body { width: 1200px; height: 854px; overflow: hidden; background: var(--paper); }
  body { font-family: "Arimo", Arial, sans-serif; color: var(--text-navy); }

  .canvas { position: relative; width: 1200px; height: 854px; overflow: hidden; }
  .sheet {
    position: absolute; left: 0; top: 0; width: 1271px; height: 904px;
    transform: scale(0.9441, 0.9447); transform-origin: 0 0;
  }
  .abs { position: absolute; }

  .crop-marks { position: absolute; left: 0; top: 0; width: 1271px; height: 904px; }

  .panel-cream { left: 37px; top: 30px; width: 790px; height: 840px; background: var(--cream); }
  .panel-sky { left: 827px; top: 30px; width: 419px; height: 840px; background: var(--sky); }

  .photo { position: absolute; }
  .photo-carer { left: 89px; top: 49px; width: 312px; height: 209px;
    background: linear-gradient(120deg, #e9d8c4 0%, #d8b89c 45%, #eef0f2 100%); }
  .photo-flower { left: 477px; top: 44px; width: 317px; height: 247px;
    background: radial-gradient(ellipse at 50% 55%, #b0325f 0%, #6b3a2c 22%, #1a1210 50%, #000 75%); }
  .photo-hands { left: 828px; top: 326px; width: 418px; height: 257px;
    background: linear-gradient(90deg, #f2f4ee 0%, #e7c8a9 40%, #c9e39a 75%, #eaf5cf 100%); }

  .services-box { left: 87px; top: 285px; width: 315px; height: 550px; background: var(--sky); }
  .services-tab { left: 85px; top: 271px; width: 162px; height: 28px; background: var(--orange);
    font-weight: 700; font-size: 22px; line-height: 28px; padding-left: 14px; color: var(--text-navy); }

  .service-detail { position: absolute; left: 120px; width: 270px; font-size: 16.5px; line-height: 20px; white-space: nowrap; }
  .service-detail .tick, .service-brief .tick { position: absolute; left: 0; top: 0; color: var(--tick); font-size: 15px; }
  .service-detail p { margin-left: 26px; }
  .service-detail strong { font-weight: 700; }

  .values { left: 87px; top: 777px; width: 315px; text-align: center; font-weight: 700; font-size: 20px; line-height: 23px; }

  .tagline-bar { left: 476px; top: 314px; width: 318px; height: 27px; background: var(--orange);
    font-weight: 700; font-size: 16px; line-height: 27px; text-align: center; }

  .brief-box { left: 477px; top: 378px; width: 317px; height: 244px; background: var(--sky); }
  .brief-tab { left: 477px; top: 364px; width: 123px; height: 28px; background: var(--orange);
    font-weight: 700; font-size: 16px; line-height: 30px; padding-left: 8px; }
  .service-brief { position: absolute; left: 509px; font-weight: 700; font-size: 16px; line-height: 20px; }
  .service-brief span.label { margin-left: 24px; }

  .call-button { left: 509px; top: 645px; width: 246px; height: 65px; background: var(--orange);
    font-weight: 700; font-size: 16px; line-height: 70px; text-align: center; }

  .contact { left: 440px; width: 390px; text-align: center; font-size: 15.5px; line-height: 18px; }
  .contact b { font-weight: 700; }

  .brand { left: 850px; top: 160px; display: flex; align-items: center; gap: 14px; }
  .brand-mark { width: 50px; height: 50px; border-radius: 50%; background: var(--navy); }
  .brand-name { font-size: 25px; font-weight: 400; color: var(--navy); line-height: 30px; white-space: nowrap; }
  .brand-line { left: 1040px; top: 204px; width: 156px; text-align: right; font-size: 15px; line-height: 18px; color: var(--orange); }

  .band { position: absolute; left: 828px; width: 418px; }
  .band-navy-top { top: 301px; height: 8px; background: var(--navy); }
  .band-orange-top { top: 309px; height: 17px; background: var(--orange); }
  .band-orange-bottom { top: 583px; height: 17px; background: var(--orange); }
  .band-navy-bottom { top: 600px; height: 8px; background: var(--navy); }

  .offer-title { left: 860px; top: 628px; font-weight: 700; font-size: 21px; white-space: nowrap; }
  .offer-list { left: 890px; top: 678px; list-style: none; font-weight: 700; font-size: 21px; line-height: 26.5px; }
  .offer-list li::before { content: "\2022"; color: var(--orange); margin-right: 12px; }
  .offer-close { left: 840px; top: 784px; width: 330px; text-align: center; font-weight: 700; font-size: 21px; line-height: 26px; }
</style>
</head>
<body>
<div class="canvas">
  <div class="sheet">
    <div class="abs panel-cream"></div>
    <div class="abs panel-sky"></div>

    <div class="photo photo-carer" role="img" aria-label="Photo of a smiling carer with an elderly man at home"></div>
    <div class="abs services-box"></div>
    <div class="abs services-tab">Our services</div>

    <div class="service-detail" style="top:318px"><span class="tick">✓</span><p><strong>Personal care-</strong> showering,<br>dressing, hygiene and<br>grooming</p></div>
    <div class="service-detail" style="top:396px"><span class="tick">✓</span><p><strong>Domestic Assistance-</strong><br>general cleaning, laundry,<br>bed linen and ironing</p></div>
    <div class="service-detail" style="top:473px"><span class="tick">✓</span><p><strong>Meal Preparation-</strong> support<br>to select, prepare and<br>enjoy meals</p></div>
    <div class="service-detail" style="top:550px"><span class="tick">✓</span><p><strong>Respite-</strong> support for carers<br>to take a well-earned break</p></div>
    <div class="service-detail" style="top:608px"><span class="tick">✓</span><p><strong>Companionship-</strong> visits,<br>social outings, transport to<br>appointments and support<br>shopping</p></div>
    <div class="service-detail" style="top:706px"><span class="tick">✓</span><p><strong>Rehabilitation-</strong> support<br>after surgery or recovering<br>from illness</p></div>

    <div class="abs values">Reliable, compassionate,<br>person centred</div>

    <div class="photo photo-flower" role="img" aria-label="Photo of cupped elderly hands holding a pink flower on black"></div>
    <div class="abs tagline-bar">Providing Exceptional Care at home</div>

    <div class="abs brief-box"></div>
    <div class="abs brief-tab">Our Services</div>
    <div class="service-brief" style="top:404px"><span class="tick">✓</span><span class="label">Personal Care</span></div>
    <div class="service-brief" style="top:438px"><span class="tick">✓</span><span class="label">Domestic Assistance</span></div>
    <div class="service-brief" style="top:473px"><span class="tick">✓</span><span class="label">Meal Preparation</span></div>
    <div class="service-brief" style="top:508px"><span class="tick">✓</span><span class="label">Respite</span></div>
    <div class="service-brief" style="top:543px"><span class="tick">✓</span><span class="label">Companionship</span></div>
    <div class="service-brief" style="top:578px"><span class="tick">✓</span><span class="label">Rehabilitation Support</span></div>

    <div class="abs call-button">CALL 1300 555 014</div>

    <div class="abs contact" style="top:737px"><b>E:</b> contact@wexfordinhomecare.com.au</div>
    <div class="abs contact" style="top:769px"><b>W</b>: wexfordinhomecare.com.au</div>
    <div class="abs contact" style="top:804px"><b>Address</b>: 12A/88 Harbour Street<br>Sydney NSW 2000</div>

    <div class="abs brand"><span class="brand-mark"></span><span class="brand-name">Wexford In Home Care</span></div>
    <div class="abs brand-line">a better way</div>

    <div class="band band-navy-top"></div>
    <div class="band band-orange-top"></div>
    <div class="photo photo-hands" role="img" aria-label="Photo of a carer's hands holding an elderly person's hand on a soft green background"></div>
    <div class="band band-orange-bottom"></div>
    <div class="band band-navy-bottom"></div>

    <div class="abs offer-title">In Home Care specialists offering</div>
    <ul class="abs offer-list">
      <li>professional</li>
      <li>non-medical</li>
      <li>companion based care</li>
    </ul>
    <div class="abs offer-close">In the comfort and familiarity<br>of your home</div>

    <svg class="crop-marks" viewBox="0 0 1271 904" aria-hidden="true">
      <g stroke="var(--crop)" stroke-width="1" fill="none">
        <line x1="52" y1="0" x2="52" y2="30"/><line x1="1218" y1="0" x2="1218" y2="30"/>
        <line x1="52" y1="874" x2="52" y2="904"/><line x1="1218" y1="874" x2="1218" y2="904"/>
        <line x1="0" y1="52" x2="34" y2="52"/><line x1="1250" y1="52" x2="1271" y2="52"/>
        <line x1="0" y1="853" x2="34" y2="853"/><line x1="1250" y1="853" x2="1271" y2="853"/>
        <circle cx="635" cy="15" r="8"/><line x1="603" y1="15" x2="667" y2="15"/><line x1="635" y1="0" x2="635" y2="30"/>
        <circle cx="635" cy="887" r="8"/><line x1="603" y1="887" x2="667" y2="887"/><line x1="635" y1="872" x2="635" y2="904"/>
        <circle cx="16" cy="452" r="8"/><line x1="0" y1="452" x2="34" y2="452"/><line x1="16" y1="420" x2="16" y2="484"/>
        <circle cx="1255" cy="452" r="8"/><line x1="1238" y1="452" x2="1271" y2="452"/><line x1="1255" y1="420" x2="1255" y2="484"/>
      </g>
    </svg>
  </div>
</div>
</body>
</html>
```